Brightmere Commercial Cleaning - Company OverView

I require a 3 page, A4 company folding proschure. I would like to convey a eco frienddly and professional service. Text and images can be found on our company web page www.brightmerecleaning.com.au however we may need some more eco friendly images to convey the right message

The broschure must highlight our companys ISO certification. We are a professional service targeting the corporate industry.

I have hi res images to send and also endorsement and certification logos to send through.

Designer may need to suppl;y some contact and images.

We would like to work with someoe frquently
Updates

HI TEAM, I AM SORRY FOR ANY CONFUSION. I HAVE JUST HAD INSTRUCTIONS THAT THE BROSCHURE WILL NEED TO BE AN A3 SIZE BUT DESIGNED WITH 2 A4 PAGES FRONT AND BACK. SORRY FOR ANY INCONVENIENCE

Target Market(s)

* Corporate
* Professional

Industry/Entity Type

Professional Service

Requirements
Must have
• * Environmental Feel
* Strong Prescense
* Must be CLEAN
* Have 6 A4 pages (Must be a 3 page a4 broschure, Double sided).
Should not have
• * Busy Text
* Old Font

```html
<!DOCTYPE html>
<html lang="en">
<head>
<meta charset="utf-8">
<title>Brightmere Commercial Cleaning – Company Overview</title>
<link rel="stylesheet" href="https://fonts.googleapis.com/css2?family=Arimo:ital,wght@0,400;0,700;1,400&family=PT+Sans+Narrow&display=swap">
<style>
  :root{
    --brand-blue:#2c6fc2;
    --soft-blue:#5b9ad8;
    --body-grey:#6a6a6a;
    --ghost-grey:#efefef;
    --accent-green:#a9c93b;
    --header-line:#c9dcee;
    --paper:#ffffff;
  }
  *{margin:0;padding:0;box-sizing:border-box}
  html,body{width:1200px;height:848px;overflow:hidden;background:var(--paper)}
  body{font-family:"Arimo",Arial,sans-serif;color:var(--body-grey);font-size:11px;line-height:13.6px}
  .spread{position:relative;width:1200px;height:848px}
  .page{position:absolute;top:0;width:600px;height:848px}
  .page--left{left:0}.page--right{left:600px}
  .masthead{position:absolute;top:0;left:0;width:600px;height:44px;
    background:linear-gradient(#fff 0%,#fff 70%,#eef4fa 100%);border-bottom:2px solid var(--header-line)}
  .brand-name{position:absolute;left:68px;top:11px;font-size:18px;line-height:20px;font-weight:700;color:var(--brand-blue)}
  .tagline{position:absolute;left:198px;top:14px;font-size:12.5px;line-height:14px;color:var(--soft-blue)}
  .photo{position:absolute;top:48px;height:176px;width:600px;left:0}
  .photo--walkway{background:linear-gradient(180deg,#14263f 0%,#4e6f95 45%,#a9c0d8 70%,#3a5271 100%)}
  .photo--lounge{background:linear-gradient(100deg,#2a1d14 0%,#5b4634 35%,#9dbc3a 55%,#6f8a2c 72%,#3b2c20 100%)}
  .green-band{position:absolute;top:224px;left:0;width:600px;height:6px;background:var(--accent-green)}
  .copy{position:absolute;width:520px}
  .name{color:var(--brand-blue);font-weight:700}
  .lead{color:var(--brand-blue)}
  .section-title{position:absolute;height:90px;width:320px}
  .section-title .ghost{position:absolute;left:0;top:0;font-family:"PT Sans Narrow",sans-serif;font-size:88px;color:var(--ghost-grey);line-height:1}
  .section-title h2{position:absolute;left:0;top:36px;font-family:"PT Sans Narrow",sans-serif;font-weight:400;font-size:48px;color:var(--brand-blue);line-height:1}
  .label{position:absolute;color:var(--brand-blue)}
  .badge{position:absolute}
  ul.points{position:absolute;list-style:none;color:var(--brand-blue)}
  ul.points li{position:relative;padding-left:10px;height:18px}
  ul.points li::before{content:"";position:absolute;left:0;top:5px;width:4px;height:4px;border-radius:50%;background:var(--soft-blue)}
  .services-head{position:absolute;font-size:13.5px;line-height:16px;font-weight:700;color:var(--brand-blue)}
  em{font-style:italic;color:var(--brand-blue)}
</style>
</head>
<body>
<div class="spread">

  <section class="page page--left">
    <header class="masthead">
      <span class="brand-name">Brightmere</span>
      <span class="tagline">The Next Generation in Commercial Cleaning</span>
    </header>
    <div class="photo photo--walkway" role="img" aria-label="Photograph of a long modern airport moving walkway"></div>
    <div class="green-band"></div>

    <p class="copy lead" style="left:56px;top:256px"><span class="name">Brightmere</span> is considered one of Australia's leading Commercial Cleaning service provider, dedicated to delivering a quality service that adds value.</p>
    <p class="copy" style="left:56px;top:297px">Our business philosophy and international networks ensures we can deliver quality and cost effective cleaning solutions. Our highly skilled Management Team working across Australia and New Zealand has built a solid reputation maintaining the highest commercial cleaning standards.</p>
    <p class="copy" style="left:56px;top:350px"><span class="name">Brightmere</span>'s commitment to deliver quality is reflected in our rapidly growing clientele base and long term working relationships.</p>

    <div class="label" style="left:56px;top:392px"><span class="name">Brightmere</span> Is ISO certified across 3 International Standards</div>
    <div class="label" style="left:382px;top:392px"><span class="name">Brightmere</span> Is a member of</div>

    <svg class="badge" style="left:56px;top:416px" width="140" height="44" role="img" aria-label="Three ISO certification badges">
      <circle cx="21" cy="22" r="19" fill="#fff" stroke="#3b3f8c" stroke-width="3"/>
      <circle cx="67" cy="22" r="19" fill="#fff" stroke="#3f8a3a" stroke-width="3"/>
      <circle cx="113" cy="22" r="19" fill="#fff" stroke="#c7342d" stroke-width="3"/>
    </svg>
    <svg class="badge" style="left:396px;top:412px" width="58" height="48" role="img" aria-label="Industry association membership badge">
      <rect x="0" y="0" width="58" height="46" rx="8" fill="#ee8a2c"/>
    </svg>

    <div class="section-title" style="left:60px;top:471px">
      <span class="ghost">About</span>
      <h2>About</h2>
    </div>

    <p class="copy" style="left:56px;top:564px">Established in 1995 and initially servicing commercial and strata offices, <span class="name">Brightmere</span> has progressively developed over 15 years to build a strong client network thought Australia and New Zealand.</p>
    <p class="copy" style="left:56px;top:604px"><span class="name">Brightmere</span> now offers the highest commercial cleaning standards to commercial industry, retail and shopping centres, hotels and tertiary education facilities.</p>
    <p class="copy" style="left:56px;top:644px">Our continual commitment and dedication to delivering a quality service has enabled <span class="name">Brightmere</span> to build a solid foundation and international presence.</p>
    <p class="copy" style="left:56px;top:684px">Building relationships based on ethical conduct towards employees and clientele defines our unique working environments and is a vital key to our success.</p>
    <p class="copy lead" style="left:56px;top:724px"><span class="name">Brightmere</span> is Industry leader in the development of environmental systems and procedures and <em>a finalist in the 2010 WorkCare, Safe Practices Award.</em></p>

    <svg class="badge" style="left:56px;top:770px" width="170" height="50" role="img" aria-label="Environmental certification and safety award badges">
      <circle cx="24" cy="25" r="22" fill="#fff" stroke="#3d5a2e" stroke-width="3"/>
      <rect x="80" y="10" width="86" height="28" rx="4" fill="#f0f0f0"/>
    </svg>
  </section>

  <section class="page page--right">
    <header class="masthead">
      <span class="brand-name">Brightmere</span>
      <span class="tagline">The Next Generation in Commercial Cleaning</span>
    </header>
    <div class="photo photo--lounge" role="img" aria-label="Photograph of a modern office lounge with lime green sofas and a glass table"></div>
    <div class="green-band"></div>

    <div class="section-title" style="left:54px;top:231px">
      <span class="ghost">Culture</span>
      <h2>Culture</h2>
    </div>

    <p class="copy" style="left:52px;top:322px">Our principle to put the client first, separates us from the rest<br>Engrained within each employee are five company principles of <span class="name">Brightmere</span>.</p>
    <ul class="points" style="left:68px;top:369px">
      <li>Put the client first</li>
      <li>Lead with integrity</li>
      <li>Deliver a quality service</li>
      <li>Take personal responsibility</li>
      <li>Keep balance</li>
    </ul>
    <p class="copy" style="left:52px;top:468px">Within these principles <span class="name">Brightmere</span> has created a company that rewards dependability, integrity, safety and provides the training and development for all employees.</p>

    <div class="section-title" style="left:54px;top:509px">
      <span class="ghost">Services</span>
      <h2>Services</h2>
    </div>

    <p class="copy" style="left:52px;top:598px"><span class="name">Brightmere</span> has built a process orientated service with measurable quality control methods and procedures based on accountability.<br><span class="name">Brightmere</span> delivers a wide range of quality services, ensuring that the management of your site is handled with competence and reliability.</p>

    <div class="services-head" style="left:78px;top:667px">Services</div>
    <ul class="points" style="left:68px;top:694px">
      <li>General cleaning requirements</li>
      <li>Security – 24 hour emergency contact</li>
      <li>Consumables supply and replacement</li>
      <li>Wash room services</li>
      <li>Building maintenance</li>
      <li>Scrubbing machinery</li>
    </ul>
    <ul class="points" style="left:366px;top:694px">
      <li>Pressure washing</li>
      <li>Window cleaning</li>
      <li>Carpet care</li>
      <li>Floor maintenance</li>
      <li>Graffiti removal</li>
    </ul>
  </section>

</div>
</body>
</html>
```